Post Card Mailer Design-

Marbrook Elder Living is a subsidiary of the Marbrook Haven Group. This Post Card is specifically for the Marbrook Elder Living company and brand. Create a 4 x 6, front and back, Post Card. This Post Card will be an invitation to prospective clients and/or caring family members to join us for informative and personalized get together(s) to discuss the Senior Care Home that we are opening. It is a modern and state of the art home. Like the home, the Post Card must be eye catching, unique in its deliverables (as it doesn’t feel like a care facility) and demonstrate both attention to detail and comfort. Our organization is sophisticated and built around warmth, care and individualized personal attention. The most important aspect of this design is to focus on creating a nurturing, warm, and inviting feel that would attract a prospective client to want to join us for an educational event.

I am open to the creativity of the designer to develop something based on the above criteria; however I would like the design to work well with our existing collateral material. What I mean by that is that while I want everything to have its own personality and stand out as its own brand representative, I still need to be able to tell that the overall design concept stays stylistically inside of the same ‘family’ of existing designed material. Because of this, I would like for the designer to pull inspiration from the link to our website (Located below) as well as from our recently refreshed business cards (Attached Below). This should allow the Post Card design to be unique and creative, while still staying inside of a framework and the feel/style that I am looking for.

Finally, I want all the designers to understand that this Post Card design is for an educational and informative, small sized event where we are looking to attract attendance from prospective clients and/or caring family members of active, positive, and happy seniors/elders. We are responsible for providing personalized care for a culturally and ethnically diverse make-up of active, positive, and happy seniors/elders. The photos that are used must be tasteful, graceful, and elegant.
Updates

Industry/Entity Type

It Company

Requirements
Must have
• • The company logo must be included.•
• Look under the Marbrook Elder Living tab at www.marbrookhavengroup.net.

```html
<!DOCTYPE html>
<html lang="en">
<head>
<meta charset="utf-8">
<title>Marbrook Elder Living – Invitation Postcard</title>
<link href="https://fonts.googleapis.com/css2?family=Righteous&family=Arimo:wght@400;700&family=Tinos:wght@400&display=swap" rel="stylesheet">
<style>
  :root{
    --stage:#262626;
    --teal-deep:#1a5668;
    --teal-mid:#1e6f86;
    --cyan:#10b4e6;
    --cyan-light:#5fd3f5;
    --grey:#d3d4d6;
    --slate:#2f4858;
    --white:#ffffff;
    --logo-ink:#4c8f99;
  }
  *{margin:0;padding:0;box-sizing:border-box}
  html,body{width:800px;height:1200px;overflow:hidden;background:var(--stage)}
  .board{position:relative;width:800px;height:1200px}
  .side-label{position:absolute;left:0;width:800px;text-align:center;color:var(--white);
    font:400 26px "Arimo",sans-serif;letter-spacing:1px}
  .abs{position:absolute}

  /* FRONT */
  .front{left:153px;top:58px;width:497px;height:577px;background:#dcdcdc;border:2px solid #bdbdbd}
  .front-info{left:10px;top:5px;width:238px;height:562px;border-radius:8px;overflow:hidden;background:var(--teal-deep)}
  .date-day{left:0;top:26px;width:238px;text-align:center;font:400 84px/1 "Righteous",sans-serif;
    color:var(--white);-webkit-text-stroke:3px var(--slate);
    text-shadow:0 0 0 var(--cyan),4px 0 0 var(--cyan),-4px 0 0 var(--cyan),0 4px 0 var(--cyan),0 -4px 0 var(--cyan)}
  .date-month{left:0;top:108px;width:238px;text-align:center;font:400 26px/1 "Righteous",sans-serif;color:var(--white)}
  .invite-band{left:0;top:150px;width:238px;height:123px;background:linear-gradient(#e6e6e8,#c5c6c8)}
  .invite-title{left:28px;top:18px;font:400 44px/1.05 "Righteous",sans-serif;color:var(--slate);letter-spacing:1px}
  .invite-title span{display:block}
  .invite-title span+span{padding-left:62px}
  .logo-box{background:var(--white);display:flex;align-items:center;justify-content:center;gap:6px;text-align:center}
  .logo-mark{width:12px;height:12px;background:var(--logo-ink);flex:none}
  .logo-name{font:400 19px/1.1 "Tinos",serif;color:var(--logo-ink)}
  .front .logo-box{left:43px;top:290px;width:149px;height:110px}
  .front-address,.front-contact{left:0;width:238px;text-align:center;color:var(--white);font:700 13.5px/18px "Arimo",sans-serif}
  .front-address{top:417px}
  .front-contact{top:481px;font-size:13px;line-height:17.5px}

  .photo-panel{width:225px;height:185px}

  /* BACK */
  .back{left:53px;top:722px;width:695px;height:418px}
  .back .logo-box{left:106px;top:110px;width:144px;height:110px}
  .back-address{left:30px;top:230px;width:300px;text-align:center;color:var(--white);font:700 14.5px/20px "Tinos",serif}
  .back-rule{left:30px;top:277px;width:296px;height:1px;background:#9fb8c0}
  .back-contact{left:30px;top:282px;width:300px;text-align:center;color:var(--white);font:400 14.5px/18.5px "Tinos",serif}
</style>
</head>
<body>
<div class="board">

  <div class="side-label" style="top:22px">FRONT</div>

  <section class="front abs" aria-label="Postcard front">
    <div class="front-info abs">
      <svg class="abs" width="238" height="562" viewBox="0 0 238 562" style="left:0;top:0" aria-hidden="true">
        <g fill="var(--cyan)" opacity=".9">
          <circle cx="200" cy="22" r="24"/><circle cx="225" cy="45" r="22"/><circle cx="178" cy="-4" r="18"/>
          <circle cx="-4" cy="120" r="24"/><circle cx="28" cy="140" r="16"/>
          <circle cx="214" cy="282" r="22"/><circle cx="186" cy="292" r="14"/>
          <circle cx="12" cy="530" r="26"/><circle cx="40" cy="552" r="18"/>
        </g>
      </svg>
      <div class="date-day abs">25</div>
      <div class="date-month abs">may, 2014</div>
      <div class="invite-band abs">
        <h1 class="invite-title abs"><span>JOIN</span><span>US!</span></h1>
      </div>
      <div class="logo-box abs"><span class="logo-mark"></span><span class="logo-name">Marbrook<br>Elder Living</span></div>
      <p class="front-address abs">4870 Koa Ridge Ave.,<br>Suite 210, Honolulu,<br>HI 96817</p>
      <p class="front-contact abs">Phone : (808) 555-0142<br>Fax : (808) 555-0187<br>E-mail : dana@marbrookelder.com<br>Web : www.marbrookelder.com</p>
    </div>

    <svg class="photo-panel abs" style="left:258px;top:5px" viewBox="0 0 225 185">
      <defs><linearGradient id="pg" x1="0" y1="0" x2="1" y2="0"><stop offset="0" stop-color="var(--teal-mid)"/><stop offset="1" stop-color="var(--cyan)"/></linearGradient></defs>
      <rect width="225" height="185" fill="url(#pg)"/>
      <path d="M6,62 C60,20 150,42 218,10 L218,150 C150,176 60,158 6,178 Z" fill="#b69a78" stroke="var(--white)" stroke-width="2" role="img" aria-label="Photo of a bright living room with sofas"/>
      <g fill="#e8e8e8"><circle cx="32" cy="12" r="5"/><circle cx="212" cy="172" r="5"/></g>
    </svg>
    <svg class="photo-panel abs" style="left:258px;top:203px;height:165px" viewBox="0 0 225 165">
      <rect width="225" height="165" fill="url(#pg)"/>
      <path d="M6,60 C60,20 150,40 218,12 L218,125 C150,150 60,135 6,150 Z" fill="#8c5a48" stroke="var(--white)" stroke-width="2" role="img" aria-label="Photo of a modern kitchen with wood cabinets"/>
      <g fill="#e8e8e8"><circle cx="32" cy="12" r="5"/><circle cx="212" cy="152" r="5"/></g>
    </svg>
    <svg class="photo-panel abs" style="left:258px;top:380px" viewBox="0 0 225 185">
      <rect width="225" height="185" fill="url(#pg)"/>
      <path d="M6,62 C60,20 150,42 218,10 L218,150 C150,176 60,158 6,178 Z" fill="#c9a77d" stroke="var(--white)" stroke-width="2" role="img" aria-label="Photo of a furnished bedroom with a patio door"/>
      <g fill="#e8e8e8"><circle cx="32" cy="12" r="5"/><circle cx="212" cy="172" r="5"/></g>
    </svg>
  </section>

  <div class="side-label" style="top:672px">BACK</div>

  <section class="back abs" aria-label="Postcard back">
    <svg class="abs" width="695" height="418" viewBox="0 0 695 418" style="left:0;top:0" aria-hidden="true">
      <defs>
        <linearGradient id="bg" x1="0" y1="0" x2="1" y2="0"><stop offset="0" stop-color="var(--teal-mid)"/><stop offset=".6" stop-color="var(--cyan)"/><stop offset="1" stop-color="var(--cyan)"/></linearGradient>
        <linearGradient id="gr" x1="0" y1="0" x2="1" y2="0"><stop offset="0" stop-color="#a9aaac"/><stop offset=".12" stop-color="var(--grey)"/><stop offset="1" stop-color="var(--grey)"/></linearGradient>
      </defs>
      <rect width="695" height="418" fill="url(#bg)"/>
      <path d="M0,62 L300,62 C430,62 560,60 695,0 L695,300 C560,340 420,362 340,362 L0,362 Z" fill="url(#gr)"/>
      <path d="M0,62 L300,62 C330,62 350,62 362,62 C350,150 370,250 362,362 L0,362 Z" fill="var(--teal-deep)"/>
      <path d="M0,62 L300,62 C430,62 560,60 695,0" fill="none" stroke="var(--white)" stroke-width="3"/>
      <path d="M0,418 C120,370 260,362 340,362 C460,362 580,330 695,300" fill="none" stroke="var(--white)" stroke-width="3"/>
      <g fill="#e6e6e6"><circle cx="22" cy="28" r="10"/><circle cx="620" cy="20" r="10"/><circle cx="70" cy="382" r="10"/><circle cx="645" cy="392" r="10"/></g>
    </svg>
    <div class="logo-box abs"><span class="logo-mark"></span><span class="logo-name">Marbrook<br>Elder Living</span></div>
    <p class="back-address abs">4870 Koa Ridge Ave.,<br>Suite 210, Honolulu, HI 96817</p>
    <div class="back-rule abs"></div>
    <p class="back-contact abs">Phone : (808) 555-0142<br>Fax : (808) 555-0187<br>E-mail : dana@marbrookelder.com<br>Web : www.marbrookelder.com</p>
  </section>

</div>
</body>
</html>
```